I am looking for a stand-out cover that sings out to new parents. The category is very pastel with limited compelling covers that would make me want to buy a book. This book will be used often in the first 12 months of baby's life - so must be strong enough to sit on the bedside table or on the coffee table to inspire reading. It will be a popular gift - so needs to look credible, "pick-up-able" and loveable.

The Book Title is - The Little Sprout Handbook on an Infant's Opening Months: Gentle, Research-Backed Methods for Rest, Nourishment, Protection and Growing Assurance
The Size is - 8.5 x 11 in
Book description to be provided to final design for inclusion
Some examples of book covers in this category attached. Thanks

```html
<!DOCTYPE html>
<html lang="en">
<head>
<meta charset="utf-8">
<title>The Little Sprout Handbook – Cover</title>
<link href="https://fonts.googleapis.com/css2?family=Lora:wght@500&family=Dancing+Script:wght@600&family=Source+Sans+3:wght@400&display=swap" rel="stylesheet">
<style>
  :root {
    --backdrop: #e9e5df;
    --cover-cream: #f5f0e3;
    --title-sage: #6b7a50;
    --script-rose: #d0908f;
    --subtitle-ink: #41453a;
    --author-ink: #55574a;
    --frame-taupe: #b29f86;
    --art-glow: #fbf3e4;
    --art-peach: #ecd3b8;
    --art-skin: #e2c2a2;
    --art-sage: #b9c9b3;
    --art-mist: #cfdad6;
    --wreath-lavender: #c9bddd;
    --wreath-sage: #c3cfa9;
    --wreath-butter: #efdca0;
    --wreath-rose: #ebc0c2;
    --wreath-aqua: #bcdcdc;
  }
  * { margin: 0; padding: 0; box-sizing: border-box; }
  html, body {
    width: 1200px; height: 1200px; overflow: hidden;
    background: var(--backdrop);
  }
  .cover {
    position: absolute; left: 230px; top: 72px;
    width: 740px; height: 1056px;
    background: var(--cover-cream);
  }
  .hero-art {
    position: absolute; left: 182px; top: 22px;
    width: 376px; height: 376px;
  }
  .wreath {
    position: absolute; left: 0; top: 380px;
    width: 740px; height: 620px;
  }
  .title-block {
    position: absolute; left: 0; top: 468px; width: 740px;
    text-align: center;
  }
  .title-main {
    font-family: "Lora", Georgia, serif; font-weight: 500;
    font-size: 58px; line-height: 1.12; color: var(--title-sage);
  }
  .title-script {
    font-family: "Dancing Script", cursive; font-weight: 600;
    font-size: 41px; line-height: 1.2; color: var(--script-rose);
    margin-top: 14px;
  }
  .subtitle {
    font-family: "Source Sans 3", Arial, sans-serif; font-weight: 400;
    font-size: 24px; line-height: 1.34; color: var(--subtitle-ink);
    margin-top: 26px;
  }
  .author {
    position: absolute; left: 0; top: 996px; width: 740px;
    text-align: center;
    font-family: "Lora", Georgia, serif; font-size: 21px;
    color: var(--author-ink);
  }
</style>
</head>
<body>
  <main class="cover">
    <svg class="hero-art" viewBox="0 0 376 376" role="img" aria-label="Watercolour illustration of two parents cradling a newborn baby inside a round frame">
      <defs>
        <radialGradient id="heroWash" cx="50%" cy="58%" r="62%">
          <stop offset="0%" stop-color="var(--art-glow)"/>
          <stop offset="35%" stop-color="var(--art-peach)"/>
          <stop offset="65%" stop-color="var(--art-skin)"/>
          <stop offset="85%" stop-color="var(--art-sage)"/>
          <stop offset="100%" stop-color="var(--art-mist)"/>
        </radialGradient>
      </defs>
      <circle cx="188" cy="188" r="176" fill="url(#heroWash)"/>
      <circle cx="188" cy="188" r="183" fill="none" stroke="var(--frame-taupe)" stroke-width="3.5"/>
      <circle cx="188" cy="188" r="176" fill="none" stroke="var(--frame-taupe)" stroke-width="1.4"/>
    </svg>

    <svg class="wreath" viewBox="0 0 740 620" role="img" aria-label="Hand-drawn wreath of daisies, lavender sprigs and pastel petals framing the title">
      <defs>
        <linearGradient id="wreathWash" x1="0" y1="0" x2="1" y2="1">
          <stop offset="0%" stop-color="var(--wreath-aqua)"/>
          <stop offset="25%" stop-color="var(--wreath-lavender)"/>
          <stop offset="50%" stop-color="var(--wreath-sage)"/>
          <stop offset="70%" stop-color="var(--wreath-butter)"/>
          <stop offset="100%" stop-color="var(--wreath-rose)"/>
        </linearGradient>
      </defs>
      <path d="M60 20 C20 250 80 470 250 560 C320 598 420 598 490 560 C660 470 720 250 680 20
               L635 40 C662 240 612 425 472 502 C410 534 330 534 268 502 C128 425 78 240 105 40 Z"
            fill="url(#wreathWash)" opacity="0.85"/>
    </svg>

    <section class="title-block">
      <h1 class="title-main">The Little Sprout<br>Handbook</h1>
      <p class="title-script">on an Infant's Opening Months</p>
      <p class="subtitle">Gentle, Research-Backed Methods<br>for Rest, Nourishment, Protection<br>and Growing Assurance</p>
    </section>

    <p class="author">By [Author Name]</p>
  </main>
</body>
</html>
```